Honey Jar Label Design

I am looking for a fun label design for a 1 lb honey jar.
The company is Rosalind Oakhurst Botanicals, which sells cut flowers and is expanding into honey and eventually other honey products. I've included the design work for the business, and I'd like the honey products to coordinate with them but not necessarily match directly.
Label requirements:
Raw Honey
Rosalind Oakhurst Botanicals
27308 Pebble Hollow Rd
Alder Glen, OR 66841
NET WT. 16 OZ. (weight info must be in the lower third of the front label and easy to read)
Look and feel
Each slider illustrates characteristics of the customer's brand and the style your logo design should communicate.

```html
<!DOCTYPE html>
<html lang="en">
<head>
<meta charset="utf-8">
<title>Raw Honey – Rosalind Oakhurst Botanicals</title>
<link rel="stylesheet" href="https://fonts.googleapis.com/css2?family=Caveat:wght@400&family=Titillium+Web:wght@400;700&family=Lato:wght@400&display=swap">
<style>
  :root {
    --ink-teal: #102b33;
    --label-white: #ffffff;
    --page: #ffffff;
    --gold: #e0c98a;
    --rule: #111111;
    --sprig-light: #1d3d46;
  }
  * { box-sizing: border-box; margin: 0; padding: 0; }
  html, body { width: 1200px; height: 800px; overflow: hidden; background: var(--page); }
  .canvas { position: relative; width: 1200px; height: 800px; }

  .dimension { position: absolute; left: 360px; top: 240px; width: 200px; height: 430px; }
  .dimension-label {
    position: absolute; left: 378px; top: 444px;
    transform: translate(-50%, -50%) rotate(-90deg);
    font-family: "Lato", sans-serif; font-size: 30px; color: var(--rule);
    white-space: nowrap; letter-spacing: 1px;
  }

  .front-label { position: absolute; left: 452px; top: 248px; width: 260px; height: 410px; }
  .front-label svg { position: absolute; inset: 0; }

  .product-title {
    position: absolute; left: 0; width: 100%; text-align: center;
    font-family: "Caveat", cursive; font-weight: 400; color: var(--label-white); line-height: 0.9;
  }
  .product-title.raw { top: 22px; font-size: 74px; }
  .product-title.honey { top: 80px; font-size: 80px; }

  .botanical-art {
    position: absolute; left: 10px; top: 155px; width: 240px; height: 105px;
    border-radius: 8px;
    background: radial-gradient(ellipse at 50% 60%, var(--sprig-light), var(--ink-teal) 75%);
  }

  .maker {
    position: absolute; left: 0; width: 100%; text-align: center;
    font-family: "Titillium Web", sans-serif; color: var(--label-white);
  }
  .maker-name { top: 271px; font-size: 16px; font-weight: 700; }
  .maker-address { top: 297px; font-size: 14px; font-weight: 400; line-height: 1.35; }

  .net-weight {
    position: absolute; left: 0; top: 362px; width: 100%; text-align: center;
    font-family: "Titillium Web", sans-serif; font-weight: 700; font-size: 22px;
    color: var(--ink-teal);
  }

  .lid-caption {
    position: absolute; left: 920px; top: 80px; transform: translateX(-50%);
    font-family: "Lato", sans-serif; font-size: 12.5px; color: var(--rule); white-space: nowrap;
  }
  .lid-arrow { position: absolute; left: 700px; top: 160px; width: 115px; height: 40px; }
  .lid-label {
    position: absolute; left: 835px; top: 122px; width: 170px; height: 170px;
    border-radius: 50%; background: var(--ink-teal);
    box-shadow: 0 0 0 2px #e6e6e6;
    display: flex; align-items: center; justify-content: center; text-align: center;
    padding: 0 26px;
  }
  .lid-name {
    font-family: "Titillium Web", sans-serif; font-weight: 700; font-size: 17px;
    line-height: 1.2; color: var(--label-white);
  }
</style>
</head>
<body>
<main class="canvas">

  <svg class="dimension" viewBox="0 0 200 430" aria-hidden="true">
    <line x1="15" y1="8" x2="195" y2="8" stroke="#111" stroke-width="1"/>
    <line x1="15" y1="418" x2="195" y2="418" stroke="#111" stroke-width="1"/>
    <line x1="18" y1="30" x2="18" y2="130" stroke="#111" stroke-width="4"/>
    <polygon points="18,14 4,36 18,30 32,36" fill="#111"/>
    <line x1="18" y1="285" x2="18" y2="395" stroke="#111" stroke-width="4"/>
    <polygon points="18,412 4,390 18,396 32,390" fill="#111"/>
  </svg>
  <div class="dimension-label">3.94 IN</div>

  <section class="front-label" aria-label="Front jar label">
    <svg viewBox="0 0 260 410" aria-hidden="true">
      <path d="M70,2 Q130,-2 190,2 C225,5 258,110 258,210 C258,280 245,340 230,390 Q225,405 205,406 L55,406 Q35,405 30,390 C15,340 2,280 2,210 C2,110 35,5 70,2 Z"
            fill="var(--label-white)" stroke="var(--ink-teal)" stroke-width="3"/>
      <path d="M70,2 Q130,-2 190,2 C225,5 258,110 258,210 C258,280 252,320 246,335 Q242,346 225,346 L35,346 Q18,346 14,335 C8,320 2,280 2,210 C2,110 35,5 70,2 Z"
            fill="var(--ink-teal)"/>
    </svg>
    <h1 class="product-title raw">Raw</h1>
    <h1 class="product-title honey">Honey</h1>
    <div class="botanical-art" role="img" aria-label="Line drawing of wildflowers, leafy sprigs and a honeybee in white on dark teal"></div>
    <p class="maker maker-name">Rosalind Oakhurst Botanicals</p>
    <p class="maker maker-address">27308 Pebble Hollow Rd,<br>Alder Glen, OR 66841</p>
    <p class="net-weight">NET WT. 16 OZ.</p>
  </section>

  <svg class="lid-arrow" viewBox="0 0 115 40" aria-hidden="true">
    <path d="M4,8 C20,8 22,22 38,18 C54,14 56,6 70,14 C80,20 86,24 94,22"
          fill="none" stroke="var(--gold)" stroke-width="6" stroke-linecap="round"/>
    <polygon points="113,20 90,6 96,22 88,36" fill="var(--gold)"/>
  </svg>

  <p class="lid-caption">diameter "1.38 – Round Lid Label</p>
  <div class="lid-label" aria-label="Round lid label">
    <span class="lid-name">Rosalind Oakhurst Botanicals</span>
  </div>

</main>
</body>
</html>
```